New Electrical Business Card Design

I would like a new design for my business cards.
i would like the same logo and font but new design
Please see attached files for front and back design.
large image can be used for graphics.
I would like the instagram link incorporated to back of card.
website site address needs to be changed to www.tidemarkelectrical.au
everything else stays as is

```html
<!DOCTYPE html>
<html lang="en">
<head>
<meta charset="utf-8">
<title>Tidemark Electrical &amp; Data – Business Card</title>
<link rel="stylesheet" href="https://fonts.googleapis.com/css2?family=Montserrat:wght@400;500;600;800;900&display=swap">
<style>
  :root {
    --backdrop: #262626;
    --card-front: #ffffff;
    --card-back: #2c2c2c;
    --ink: #1d1d1b;
    --grey: #6b6b6b;
    --green: #0f7a3c;
    --faint: #f1f1f1;
    --back-mark: #1b1b1b;
    --back-text: #f2f2f2;
  }
  * { margin: 0; padding: 0; box-sizing: border-box; }
  html, body { width: 1200px; height: 1059px; overflow: hidden; }
  body {
    background: var(--backdrop);
    font-family: "Montserrat", sans-serif;
    position: relative;
  }
  .card {
    position: absolute;
    border-radius: 24px;
    overflow: hidden;
    box-shadow: 0 10px 24px rgba(0,0,0,.45);
  }
  .card--front { left: 256px; top: 89px; width: 688px; height: 390px; background: var(--card-front); }
  .card--back  { left: 254px; top: 547px; width: 693px; height: 393px; background: var(--card-back); }

  .backdrop-circle {
    position: absolute; left: 360px; top: 58px;
    width: 312px; height: 312px; border-radius: 50%;
    background: var(--faint);
  }
  .brand { position: absolute; color: var(--ink); font-weight: 900; line-height: 1; }
  .brand__name { display: block; letter-spacing: 1px; }
  .brand__tag { display: block; letter-spacing: 0.5px; }
  .card--front .brand { left: 32px; top: 72px; }
  .card--front .brand__name { font-size: 40px; }
  .card--front .brand__tag { font-size: 12px; margin-top: 6px; padding-left: 150px; }

  .person {
    position: absolute; left: 32px; top: 183px;
    font-size: 21px; font-weight: 600; letter-spacing: 0.5px; color: var(--grey);
  }
  .person__first { color: var(--green); font-weight: 800; }

  .contacts { position: absolute; left: 31px; top: 224px; list-style: none; }
  .contacts li {
    display: flex; align-items: center; gap: 6px;
    height: 26.5px; font-size: 17px; color: var(--ink);
  }
  .contacts svg { width: 14px; height: 14px; fill: var(--green); flex: none; }

  .registration {
    position: absolute; left: 32px; top: 315px;
    font-size: 17px; line-height: 22px; color: var(--ink);
  }
  .services {
    position: absolute; left: 422px; top: 312px;
    font-size: 17px; font-weight: 600; line-height: 18px; color: var(--ink);
  }
  .services p { margin-bottom: 0; height: 18px; }
  .services .dot { color: var(--green); font-size: 12px; padding: 0 4px 0 0; vertical-align: 2px; }

  .card--back .brand { left: 0; right: 0; top: 150px; text-align: center; color: var(--back-mark); }
  .card--back .brand__name { font-size: 58px; }
  .card--back .brand__tag { font-size: 17px; margin-top: 8px; padding-left: 170px; }

  .social {
    position: absolute; left: 0; right: 0; top: 333px;
    display: flex; justify-content: center; align-items: center; gap: 9px;
    font-size: 20px; color: var(--back-text); letter-spacing: 0.3px;
  }
  .social__marker { width: 14px; height: 14px; border-radius: 50%; border: 2px solid var(--green); }
</style>
</head>
<body>
  <section class="card card--front">
    <div class="backdrop-circle" aria-hidden="true"></div>

    <div class="brand">
      <span class="brand__name">TIDEMARK</span>
      <span class="brand__tag">ELECTRICAL &amp; DATA</span>
    </div>

    <h1 class="person"><span class="person__first">DANIEL</span> WHITCOMBE</h1>

    <ul class="contacts">
      <li>
        <svg viewBox="0 0 24 24" aria-hidden="true"><path d="M6.6 10.8a15.1 15.1 0 0 0 6.6 6.6l2.2-2.2c.3-.3.7-.4 1-.2 1.1.4 2.3.6 3.6.6.6 0 1 .4 1 1V20c0 .6-.4 1-1 1A17 17 0 0 1 3 4c0-.6.4-1 1-1h3.5c.6 0 1 .4 1 1 0 1.3.2 2.5.6 3.6.1.3 0 .7-.2 1z"/></svg>
        0400 123 987
      </li>
      <li>
        <svg viewBox="0 0 24 24" aria-hidden="true"><path d="M2 5h20v14H2zm2 2v.4l8 5.2 8-5.2V7z"/></svg>
        info@tidemarkelectrical.au
      </li>
      <li>
        <svg viewBox="0 0 24 24" aria-hidden="true"><circle cx="12" cy="12" r="10"/></svg>
        www.tidemarkelectrical.au
      </li>
    </ul>

    <div class="registration">
      <p>ABN - 12 345 678 901</p>
      <p>Lic Number - 100482C</p>
    </div>

    <div class="services">
      <p><span class="dot">●</span>Residential <span class="dot">●</span>Commercial</p>
      <p><span class="dot">●</span>Industrial <span class="dot">●</span>24hr Service</p>
    </div>
  </section>

  <section class="card card--back">
    <div class="brand">
      <span class="brand__name">TIDEMARK</span>
      <span class="brand__tag">ELECTRICAL &amp; DATA</span>
    </div>
    <p class="social"><span class="social__marker" aria-hidden="true"></span>tidemark.electrical</p>
  </section>
</body>
</html>
```